Vindmark Health & Wellness needs a fresh and interesting website

I need a rebrand and redevelopment of my website, www.dellaquorne.example
Our mission is provide bespoke , lifestyle medicine , everyone has their own path to health. and we are creating a personalized experience for people to life their life to the fullest
Vindmark - means sea lands
I need an landing page and about page and potentially a few project launch pages , I have been using Wordpress for my basic information and then I use Plovix for the launch pages of my programs since I can edit those easily.

Target Market(s)

Corporate and individual's who are interested in a different perspective on health and wellness , and living with a chronic illness

Industry/Entity Type

Health, lifestyle , wellness coaching and medicine

Coding

Number of Pages Required

Font styles to use
Other font styles liked:
• look into the logo

Requirements
Must have
• the logo I uploaded
Nice to have
• I want a fresh perspective on health, I have bamboo, hibiscus vibes in my logo , but also like more of a water vibe/ I want something earthy but not too boho it needs to be clean
Should not have
• every other holistic health vibe,

```html
<!DOCTYPE html>
<html lang="en">
<head>
<meta charset="utf-8">
<title>Vindmark Health &amp; Wellness</title>
<link href="https://fonts.googleapis.com/css2?family=Poppins:wght@400;500;600&family=Tinos&display=swap" rel="stylesheet">
<style>
:root{
  --teal-dark:#0d5f78;
  --teal:#15799a;
  --teal-bright:#1a8fb0;
  --green:#6aaa1c;
  --green-light:#e9f8cf;
  --mint:#fafdf3;
  --ink:#333a3f;
  --muted:#55606a;
  --field:#f7f7f7;
  --white:#ffffff;
}
*{margin:0;padding:0;box-sizing:border-box}
html,body{width:1200px;height:4655px;overflow:hidden}
body{position:relative;font-family:"Poppins",sans-serif;color:var(--ink);background:var(--white)}
.abs{position:absolute}
.btn{position:absolute;display:flex;align-items:center;justify-content:space-between;border-radius:40px;background:var(--teal-dark);color:var(--white);font-weight:500;text-transform:uppercase;white-space:nowrap}
.btn .chev{display:flex;align-items:center;justify-content:center;border-radius:50%;border:2px solid var(--white);background:var(--green);color:var(--white);font-weight:600}
.section-title{position:absolute;left:0;width:1200px;text-align:center;font-weight:500;color:var(--teal-dark)}

/* header */
.site-header{top:0;left:0;width:1200px;height:123px;background:var(--white)}
.brand{display:flex;align-items:center;gap:14px}
.brand-dot{border-radius:50%;background:var(--teal)}
.brand-name{font-weight:500;color:var(--teal)}
.search-pill{left:611px;top:0;width:260px;height:45px;background:var(--teal-dark);border-radius:0 0 0 30px;color:var(--white);font-size:14px;padding:12px 0 0 62px}
.search-pill .dot{position:absolute;left:186px;top:14px;width:18px;height:18px;border-radius:50%;border:2px solid var(--white)}
.social-bar{left:849px;top:0;width:351px;height:45px;background:var(--green);border-radius:0 0 0 30px;color:var(--white);font-size:14px;display:flex;align-items:center;gap:26px;padding-left:46px}
.social-bar span{display:flex;align-items:center;gap:8px}
.social-bar i{width:24px;height:24px;border-radius:50%;background:var(--white);display:block}
.main-nav{top:74px;left:537px;display:flex;gap:33px;font-size:12.5px;color:var(--ink)}
.main-nav a{color:inherit;text-decoration:none;padding-bottom:8px}
.main-nav a.active{color:var(--green);border-bottom:2px solid var(--green)}

/* hero */
.hero{top:123px;left:0;width:1200px;height:717px;background:var(--green-light)}
.hero-visual{left:530px;top:30px;width:670px;height:600px;background:linear-gradient(135deg,#d6efb0,#c4e29c 55%,#dcefc0)}
.welcome{left:76px;top:164px;width:307px;height:42px;border-radius:22px;background:var(--green);color:var(--white);font-family:"Tinos",serif;font-size:27px;padding:3px 0 0 43px}
.hero-title{left:74px;top:218px;font-family:"Tinos",serif;font-weight:400;font-size:92px;color:var(--teal-dark);line-height:1}
.hero-sub{left:76px;top:320px;font-family:"Tinos",serif;font-size:50px;color:var(--teal-dark);line-height:1}
.hero .btn{left:76px;top:415px;width:226px;height:73px;font-size:17px;padding:0 14px 0 39px}
.hero .btn .chev{width:40px;height:40px;font-size:15px}
.dots{left:549px;top:628px;display:flex;gap:12px;align-items:center}
.dots i{width:11px;height:11px;border-radius:50%;background:#c5cdb8;display:block}
.dots i.on{width:28px;height:7px;border-radius:4px;background:var(--teal)}

/* about */
.about-photo-frame{left:157px;top:949px;width:380px;height:428px;background:var(--white);border-radius:30px 4px 30px 4px;box-shadow:0 4px 16px rgba(0,0,0,.18)}
.about-photo{left:167px;top:962px;width:360px;height:402px;border-radius:24px 0 24px 0;background:linear-gradient(160deg,#6e8a4e,#9a8f80 55%,#b8ad9c)}
.about-title{left:604px;top:973px;font-size:40px;font-weight:500;color:var(--teal-dark)}
.about-text{left:604px;top:1064px;width:468px;font-size:13.5px;line-height:22.5px;color:var(--muted);text-align:justify}
.about-text p+p{margin-top:18px}
.about .btn{left:605px;top:1281px;width:163px;height:51px;font-size:13px;padding:0 8px 0 27px}
.about .btn .chev{width:30px;height:30px;font-size:11px}

/* why */
.why{top:1491px;left:0;width:1200px;height:542px;background:var(--mint)}
.feature{position:absolute;width:220px;text-align:center}
.feature .badge{width:104px;height:104px;border-radius:50%;margin:0 auto;display:flex;align-items:center;justify-content:center;border:3px solid var(--white);box-shadow:0 0 0 2px rgba(0,0,0,.06)}
.feature .badge.teal{background:var(--teal-dark)}
.feature .badge.green{background:var(--green)}
.feature h3{margin-top:22px;font-size:21px;font-weight:500;color:var(--teal)}
.feature p{margin-top:8px;font-size:13.5px;line-height:21px;color:var(--muted)}

/* services */
.service{position:absolute;top:2270px;width:285px;height:363px;background:var(--white);box-shadow:0 2px 12px rgba(0,0,0,.14);text-align:center}
.service .thumb{margin:7px;height:163px}
.service h3{margin-top:34px;font-size:23px;font-weight:500;color:var(--teal)}
.service p{margin:12px 26px 0;font-size:13.5px;line-height:22.5px;color:var(--muted)}
.service .btn{left:78px;top:341px;width:130px;height:37px;font-size:11px;padding:0 6px 0 20px}
.service .btn .chev{width:26px;height:26px;font-size:10px}
.slide-arrow{position:absolute;width:41px;height:41px;border-radius:50%;display:flex;align-items:center;justify-content:center;font-size:18px;font-weight:600}

/* reviews */
.reviews{top:2788px;left:0;width:1200px;height:633px;background:linear-gradient(180deg,var(--teal-bright),var(--teal-dark))}
.review{position:absolute;top:3032px;width:286px;height:222px;border:2px solid var(--green);padding:22px 22px 0 22px;color:var(--white)}
.review .who{display:flex;align-items:center;gap:16px}
.review .avatar{width:74px;height:74px;border-radius:50%;border:3px solid var(--white);background:linear-gradient(160deg,#d8c6b4,#8a7466)}
.review h4{font-size:14px;font-weight:500}
.review small{display:block;font-size:10px;margin-top:2px}
.review .stars{font-size:11px;letter-spacing:1px;margin-top:6px}
.review p{margin-top:16px;font-size:10.5px;line-height:18px;text-align:justify}

/* contact */
.field{position:absolute;background:var(--field);box-shadow:0 1px 6px rgba(0,0,0,.1);font-size:13px;color:#9a9fa4;padding:14px 20px}
.contact .btn{left:117px;top:4003px;width:174px;height:54px;font-size:13px;padding:0 10px 0 25px}
.contact .btn .chev{width:30px;height:30px;font-size:11px}
.contact-visual{left:632px;top:3659px;width:480px;height:416px;background:linear-gradient(135deg,#a6c97a,#7ea654 60%,#93b86a)}

/* footer */
.site-footer{top:4180px;left:0;width:1200px;height:410px;background:var(--teal-bright);color:var(--white)}
.footer-brand{left:0;top:4300px;width:1200px;display:flex;justify-content:center;align-items:center;gap:16px}
.footer-brand .brand-dot{background:var(--white)}
.footer-brand .brand-name{color:var(--white)}
.rule{left:78px;width:1051px;height:1px;background:rgba(255,255,255,.55)}
.footer-contact{top:4436px;display:flex;align-items:flex-start;gap:14px;font-size:13.5px;line-height:18px;color:var(--white)}
.footer-contact svg{flex:none}
.footer-nav{top:4534px;left:0;width:1200px;display:flex;justify-content:center;gap:44px;font-size:12.5px;color:var(--white)}
.copy-bar{top:4590px;left:0;width:1200px;height:65px;background:var(--green);color:var(--white);font-size:12px}
.copy-bar .txt{position:absolute;left:76px;top:24px}
.copy-bar .icons{position:absolute;left:990px;top:20px;display:flex;gap:12px}
.copy-bar .icons i{display:block;width:24px;height:24px;border-radius:50%;background:var(--teal)}
</style>
</head>
<body>

<header class="abs site-header">
  <div class="abs brand" style="left:72px;top:40px">
    <span class="brand-dot" style="width:58px;height:58px"></span>
    <span class="brand-name" style="font-size:25px;line-height:1.1">Vindmark<br><span style="font-size:11px;letter-spacing:3px">HEALTH &amp; WELLNESS</span></span>
  </div>
  <div class="abs search-pill">Search<span class="dot"></span></div>
  <div class="abs social-bar"><span><i></i>Follow</span><span><i></i>Gallery</span></div>
  <nav class="abs main-nav">
    <a class="active">HOME</a><a>ABOUT US</a><a>FALL MINI RETREAT</a><a>SERVICES</a><a>TESTIMONIALS</a><a>CONTACT</a>
  </nav>
</header>

<section class="abs hero">
  <div class="abs hero-visual" role="img" aria-label="Photo of a potted plant with long green leaves seen from above"></div>
  <div class="abs welcome">Welcome to</div>
  <h1 class="abs hero-title">VINDMARK</h1>
  <div class="abs hero-sub">Health &amp; Wellness</div>
  <a class="btn">Know More <span class="chev">&gt;&gt;</span></a>
  <div class="abs dots"><i class="on"></i><i></i><i></i><i></i></div>
</section>

<section class="about">
  <div class="abs about-photo-frame"></div>
  <div class="abs about-photo" role="img" aria-label="Portrait of the doctor sitting on garden steps"></div>
  <h2 class="abs about-title">About Us</h2>
  <div class="abs about-text">
    <p>At a young age, I discovered the transformative power of Eastern Medicine when it helped me overcome lung concerns, propelling me toward my dreams as a young athlete. Years later, I faced a pivotal choice: How could I best serve and heal my community? The answer was crystal clear—Eastern Medicine.</p>
    <p>As an Eastern Medicine doctor, I’ve had the privilege of positively impacting my community through integrative health choices.</p>
  </div>
  <a class="btn">Read More <span class="chev">&gt;&gt;</span></a>
</section>

<section class="abs why"></section>
<h2 class="section-title" style="top:1602px;font-size:52px">Why Choose Us?</h2>
<div class="feature" style="left:134px;top:1724px">
  <div class="badge teal"><svg width="52" height="52" viewBox="0 0 52 52" fill="none" stroke="#fff" stroke-width="2.4" stroke-linecap="round" stroke-linejoin="round"><circle cx="26" cy="18" r="11"/><path d="M21 18l4 4 7-8"/><path d="M6 34l8 10h10M46 34l-8 10H28"/></svg></div>
  <h3>Certified</h3><p>Lorem ipsum dolor sit amet, con sectetur adipiscing elit.</p>
</div>
<div class="feature" style="left:369px;top:1724px">
  <div class="badge green"><svg width="52" height="52" viewBox="0 0 52 52" fill="none" stroke="#fff" stroke-width="2.4" stroke-linecap="round" stroke-linejoin="round"><circle cx="26" cy="14" r="8"/><path d="M22 14l3 3 5-6"/><path d="M4 28l10-4 8 4 8-4 8 4 10-4M14 24l10 14h4l10-14"/></svg></div>
  <h3>Commitment</h3><p>Lorem ipsum dolor sit amet, con sectetur adipiscing elit.</p>
</div>
<div class="feature" style="left:607px;top:1724px">
  <div class="badge teal"><svg width="52" height="52" viewBox="0 0 52 52" fill="none" stroke="#fff" stroke-width="2.4" stroke-linecap="round" stroke-linejoin="round"><circle cx="24" cy="16" r="9"/><path d="M8 46c0-10 7-16 16-16s16 6 16 16"/><circle cx="38" cy="38" r="7"/><path d="M35 38l2 2 4-4"/></svg></div>
  <h3>Professional Expert</h3><p>Lorem ipsum dolor sit amet, con sectetur adipiscing elit.</p>
</div>
<div class="feature" style="left:846px;top:1724px">
  <div class="badge green"><svg width="52" height="52" viewBox="0 0 52 52" fill="none" stroke="#fff" stroke-width="2.4" stroke-linecap="round" stroke-linejoin="round"><circle cx="26" cy="26" r="20"/><circle cx="26" cy="21" r="6"/><path d="M16 36c2-6 6-8 10-8s8 2 10 8"/></svg></div>
  <h3>24/7 Support</h3><p>Lorem ipsum dolor sit amet, con sectetur adipiscing elit.</p>
</div>

<h2 class="section-title" style="top:2146px;font-size:52px">Our Services</h2>
<div class="slide-arrow" style="left:72px;top:2450px;border:2px solid var(--ink);color:var(--ink)">&lsaquo;</div>
<div class="slide-arrow" style="left:1088px;top:2450px;background:#555;color:#fff">&rsaquo;</div>
<div class="service" style="left:145px">
  <div class="thumb" role="img" aria-label="Photo of a woman meditating by a river" style="background:linear-gradient(180deg,#7c9a4a,#b5b0a4)"></div>
  <h3>Meditation</h3><p>Lorem ipsum dolor sit amet, consectetur adipiscing elit, sed do eiusmod tempor incididunt ut</p>
  <a class="btn">Read More <span class="chev">&gt;&gt;</span></a>
</div>
<div class="service" style="left:459px">
  <div class="thumb" role="img" aria-label="Photo of two hands clasped in support" style="background:linear-gradient(160deg,#f3ddd0,#d9b4a0 60%,#8a817a)"></div>
  <h3>Healing</h3><p>Lorem ipsum dolor sit amet, consectetur adipiscing elit, sed do eiusmod tempor incididunt ut</p>
  <a class="btn">Read More <span class="chev">&gt;&gt;</span></a>
</div>
<div class="service" style="left:770px">
  <div class="thumb" role="img" aria-label="Photo of fresh vegetables splashing in water" style="background:linear-gradient(160deg,#eaf0f0,#8ab85a 60%,#b9604a)"></div>
  <h3>Healthy Food</h3><p>Lorem ipsum dolor sit amet, consectetur adipiscing elit, sed do eiusmod tempor incididunt ut</p>
  <a class="btn">Read More <span class="chev">&gt;&gt;</span></a>
</div>

<section class="abs reviews"></section>
<h2 class="section-title" style="top:2891px;font-size:52px;color:var(--white)">Customer Reviews</h2>
<div class="review" style="left:148px">
  <div class="who"><div class="avatar" role="img" aria-label="Reviewer portrait"></div><div><h4>Marlow Fenwick</h4><small>Sit Amet</small><div class="stars">★★★★★</div></div></div>
  <p>“Lorem ipsum dolor sit amet, consectetur adipiscing elit. Pellentesque aliquet eros vitae placerat hendrerit. Maecenas maximus commodo sapien, vitae lobortis ligula maximus eu.”</p>
</div>
<div class="review" style="left:459px">
  <div class="who"><div class="avatar" role="img" aria-label="Reviewer portrait"></div><div><h4>Odile Varga</h4><small>Sit Amet</small><div class="stars">★★★★★</div></div></div>
  <p>“Lorem ipsum dolor sit amet, consectetur adipiscing elit. Pellentesque aliquet eros vitae placerat hendrerit. Maecenas maximus commodo sapien, vitae lobortis ligula maximus eu.”</p>
</div>
<div class="review" style="left:766px">
  <div class="who"><div class="avatar" role="img" aria-label="Reviewer portrait"></div><div><h4>Teodor Blaine</h4><small>Sit Amet</small><div class="stars">★★★★★</div></div></div>
  <p>“Lorem ipsum dolor sit amet, consectetur adipiscing elit. Pellentesque aliquet eros vitae placerat hendrerit. Maecenas maximus commodo sapien, vitae lobortis ligula maximus eu.”</p>
</div>
<div class="slide-arrow" style="left:559px;top:3298px;width:33px;height:33px;border:2px solid #fff;color:#fff;font-size:16px">&lsaquo;</div>
<div class="slide-arrow" style="left:606px;top:3298px;width:33px;height:33px;background:var(--green);color:#fff;font-size:16px">&rsaquo;</div>

<section class="contact">
  <h2 class="section-title" style="top:3545px;font-size:52px">Contact Us</h2>
  <div class="field" style="left:116px;top:3701px;width:222px;height:43px">First Name:</div>
  <div class="field" style="left:358px;top:3701px;width:224px;height:43px">Last Name:</div>
  <div class="field" style="left:116px;top:3768px;width:222px;height:43px">Phone:</div>
  <div class="field" style="left:358px;top:3768px;width:224px;height:43px">Email:</div>
  <div class="field" style="left:116px;top:3833px;width:466px;height:142px;padding-top:22px">Mesage:</div>
  <a class="btn">Submit Now <span class="chev">&gt;&gt;</span></a>
  <div class="abs contact-visual" role="img" aria-label="Photo of a succulent plant in a pot seen from above"></div>
</section>

<footer class="abs site-footer"></footer>
<div class="abs footer-brand">
  <span class="brand-dot" style="width:60px;height:60px"></span>
  <span class="brand-name" style="font-size:34px;line-height:1.1">Vindmark<br><span style="font-size:12px;letter-spacing:4px">HEALTH &amp; WELLNESS</span></span>
</div>
<div class="abs rule" style="top:4411px"></div>
<div class="abs footer-contact" style="left:244px"><svg width="26" height="26" viewBox="0 0 26 26"><circle cx="13" cy="13" r="13" fill="#fff"/><path d="M13 6a5 5 0 0 0-5 5c0 4 5 9 5 9s5-5 5-9a5 5 0 0 0-5-5z" fill="#1a8fb0"/><circle cx="13" cy="11" r="2" fill="#fff"/></svg><span>Address line dummy here<br>Address line dummy</span></div>
<div class="abs footer-contact" style="left:530px"><svg width="22" height="22" viewBox="0 0 24 24" fill="none" stroke="#fff" stroke-width="2"><path d="M5 3h4l2 5-3 2a12 12 0 0 0 6 6l2-3 5 2v4a2 2 0 0 1-2 2A18 18 0 0 1 3 5a2 2 0 0 1 2-2z"/></svg><span style="padding-top:3px">014-552-8370</span></div>
<div class="abs footer-contact" style="left:752px"><svg width="20" height="20" viewBox="0 0 24 24" fill="none" stroke="#fff" stroke-width="2"><rect x="2" y="5" width="20" height="14"/><path d="M2 5l10 8 10-8"/></svg><span>info@vindmark.example</span></div>
<div class="abs rule" style="top:4505px"></div>
<nav class="abs footer-nav"><span>HOME</span><span>ABOUT US</span><span>FALL MINI RETREAT</span><span>SERVICES</span><span>TESTIMONIALS</span><span>CONTACT</span></nav>
<div class="abs copy-bar"><span class="txt">Copyright © 2024 Della Quorne</span><span class="icons"><i></i><i></i><i></i><i></i></span></div>

</body>
</html>
```